Business Card Design

We need a new business card design for a company based in Southlake, TX. We provide business consulting services in the information technology / services space. We like variations of the color blue, aqua, black, light tan, and white. Would like "cool" tones. The design should clearly communicate professionalism. Think outside the box - we don't want something "typical". Our company name is "Harlow Advisory, LLC".
Updates

Thank you all for your submissions. We have seen some very creative and inspired designs. We have made a decision and will be moving forward with that design. Appreciate all of the hard work.

Industry/Entity Type

Information Technology

Contact Information for Business Card

Megan Harlow Pruett
318 West Birchfield Run Dr.
Southlake, TX 76418

```html
<!DOCTYPE html>
<html lang="en">
<head>
<meta charset="utf-8">
<title>Harlow Advisory – Business Card</title>
<link href="https://fonts.googleapis.com/css2?family=Ubuntu:wght@400;700&display=swap" rel="stylesheet">
<style>
  :root {
    --page-bg: #e6e8eb;
    --charcoal: #333333;
    --sky: #08aeea;
    --sky-deep: #1f98d9;
    --white: #ffffff;
  }
  html, body {
    margin: 0;
    width: 1200px;
    height: 1000px;
    overflow: hidden;
    background: var(--page-bg);
    font-family: "Ubuntu", sans-serif;
  }
  .card {
    position: absolute;
    left: 100px;
    top: 214px;
    width: 1000px;
    height: 572px;
    background: var(--sky);
    overflow: hidden;
    box-shadow: 0 6px 24px rgba(0,0,0,0.18);
  }
  .brand-panel {
    position: absolute;
    left: 0; top: 0;
    width: 400px; height: 100%;
    background: var(--charcoal);
  }
  .brand {
    position: absolute;
    left: 0; right: 0; top: 210px;
    text-align: center;
    color: var(--white);
  }
  .brand-mark {
    display: block;
    margin: 0 auto 22px;
    width: 70px; height: 70px;
    border: 5px solid var(--white);
    border-radius: 50%;
    box-sizing: border-box;
  }
  .brand-name {
    font-weight: 700;
    font-size: 34px;
    line-height: 40px;
    letter-spacing: 1px;
    margin: 0;
  }
  .name-band {
    position: absolute;
    left: 400px; top: 120px;
    width: 560px; height: 80px;
  }
  .name-band svg { position: absolute; inset: 0; }
  .person-name {
    position: absolute;
    left: 0; top: 0;
    height: 80px;
    line-height: 80px;
    padding-left: 0;
    margin: 0;
    color: var(--white);
    font-weight: 700;
    font-size: 28px;
    transform: translateX(-22px);
  }
  .contact-list { position: absolute; left: 400px; top: 200px; width: 600px; margin: 0; padding: 0; list-style: none; }
  .contact-row { position: relative; display: flex; align-items: center; color: var(--white); font-size: 24px; }
  .contact-row.is-phone { height: 75px; background: var(--sky); }
  .contact-row.is-email { height: 80px; background: var(--sky-deep); }
  .contact-row.is-address { height: 110px; background: var(--sky); line-height: 32px; }
  .icon-cell {
    width: 80px; height: 100%;
    display: flex; align-items: center; justify-content: center;
    background: var(--sky-deep);
    flex: none;
  }
  .contact-row.is-email .icon-cell { background: #2189cc; }
  .icon-dot {
    width: 22px; height: 22px;
    border: 3px solid var(--white);
    border-radius: 50%;
  }
  .contact-text { padding-left: 40px; }
</style>
</head>
<body>
  <div class="card">
    <div class="brand-panel">
      <div class="brand">
        <span class="brand-mark"></span>
        <p class="brand-name">HARLOW<br>ADVISORY, LLC</p>
      </div>
    </div>

    <div class="name-band">
      <svg width="560" height="80" viewBox="0 0 560 80">
        <polygon points="0,0 530,0 560,40 560,80 0,80" fill="var(--charcoal)"/>
        <polygon points="530,0 560,40 545,40" fill="#262626"/>
      </svg>
      <p class="person-name" style="left:62px">Megan Harlow Pruett</p>
    </div>

    <ul class="contact-list">
      <li class="contact-row is-phone">
        <span class="icon-cell"><span class="icon-dot"></span></span>
        <span class="contact-text">713-555-0148</span>
      </li>
      <li class="contact-row is-email">
        <span class="icon-cell"><span class="icon-dot"></span></span>
        <span class="contact-text">megan.pruett@harlowmail.com</span>
      </li>
      <li class="contact-row is-address">
        <span class="icon-cell"><span class="icon-dot"></span></span>
        <span class="contact-text">318 West Birchfield Run Dr.<br>Southlake, TX 76418</span>
      </li>
    </ul>
  </div>
</body>
</html>
```